TrovaLine.com Business Cards

Logo is attached but does not need to be used. We would prefer if the logo was just on the back of the card. We would like something creative for the front of the card.
Please see our website @ www.TrovaLine.com to get a better feel for our company.

Card should include
Name
Title
Phone #
Email Address
Address
Website

Industry/Entity Type

Events

```html
<!DOCTYPE html>
<html lang="en">
<head>
<meta charset="utf-8">
<title>TrovaLine.com Business Cards</title>
<link rel="stylesheet" href="https://fonts.googleapis.com/css2?family=Dosis:wght@400;500;700;800&display=swap">
<style>
  :root {
    --page: #ffffff;
    --card-light: #f4f4f4;
    --card-grey: #d9d9d9;
    --brand-red: #c8201e;
    --orange-deep: #e8481a;
    --orange-mid: #f26a22;
    --orange-light: #f89a4a;
    --white: #ffffff;
    --cream: #ffe6cf;
  }
  html, body {
    margin: 0;
    padding: 0;
    width: 973px;
    height: 1200px;
    overflow: hidden;
    background: var(--page);
    font-family: "Dosis", sans-serif;
  }
  .canvas {
    position: relative;
    width: 973px;
    height: 1200px;
  }
  .card-shape {
    position: absolute;
    left: 0;
    top: 0;
  }
  .logo-name {
    position: absolute;
    display: flex;
    align-items: center;
    gap: 14px;
    color: var(--brand-red);
    font-weight: 800;
    letter-spacing: 2px;
  }
  .logo-mark {
    background: var(--brand-red);
    border-radius: 4px;
  }
  .card-back .logo-name {
    left: 0;
    right: 0;
    top: 150px;
    justify-content: center;
    font-size: 78px;
  }
  .card-back .logo-mark { width: 34px; height: 34px; }
  .back-website {
    position: absolute;
    left: 0;
    right: 0;
    top: 462px;
    text-align: center;
    color: var(--white);
    font-size: 24px;
    font-weight: 500;
    letter-spacing: 1px;
  }
  .card-front .logo-name {
    left: 56px;
    top: 612px;
    font-size: 32px;
    color: var(--white);
  }
  .card-front .logo-mark { width: 16px; height: 16px; background: var(--white); }
  .front-watermark {
    position: absolute;
    left: 70px;
    top: 790px;
    font-size: 104px;
    font-weight: 800;
    letter-spacing: 2px;
    color: var(--white);
    opacity: 0.22;
  }
  .holder-name {
    position: absolute;
    right: 32px;
    top: 664px;
    margin: 0;
    font-size: 42px;
    font-weight: 500;
    color: var(--white);
    letter-spacing: 1px;
  }
  .holder-title {
    position: absolute;
    right: 34px;
    top: 716px;
    margin: 0;
    font-size: 19px;
    color: var(--white);
    letter-spacing: 1.5px;
  }
  .contact-list {
    position: absolute;
    left: 520px;
    top: 768px;
    margin: 0;
    color: var(--white);
  }
  .contact-row {
    display: grid;
    grid-template-columns: 168px 34px 240px;
    margin-bottom: 26px;
    font-size: 20px;
    line-height: 1.2;
  }
  .contact-row dt {
    text-transform: uppercase;
    letter-spacing: 3px;
    font-size: 18px;
  }
  .contact-row dd { margin: 0; color: var(--cream); }
  .contact-row .colon { color: var(--white); }
  .address { font-size: 16px; line-height: 1.3; }
</style>
</head>
<body>
<main class="canvas">

  <section class="card-back" aria-label="Card back">
    <svg class="card-shape" width="973" height="1200" viewBox="0 0 973 1200" aria-hidden="true">
      <defs>
        <radialGradient id="backFill" cx="50%" cy="35%" r="70%">
          <stop offset="0" stop-color="#ffffff"/>
          <stop offset="1" stop-color="#d6d6d6"/>
        </radialGradient>
        <linearGradient id="bandFill" x1="0" y1="0" x2="1" y2="0">
          <stop offset="0" stop-color="#e8481a"/>
          <stop offset="0.5" stop-color="#f7863a"/>
          <stop offset="1" stop-color="#e8481a"/>
        </linearGradient>
        <linearGradient id="frontFill" x1="0" y1="0" x2="1" y2="1">
          <stop offset="0" stop-color="#e63e17"/>
          <stop offset="0.6" stop-color="#f26a22"/>
          <stop offset="1" stop-color="#f58a3c"/>
        </linearGradient>
        <linearGradient id="footFill" x1="0" y1="0" x2="0" y2="1">
          <stop offset="0" stop-color="#f8a15a" stop-opacity="0"/>
          <stop offset="1" stop-color="#fbc18a" stop-opacity="0.8"/>
        </linearGradient>
      </defs>
      <path d="M0 60 Q0 0 60 0 L973 0 L973 540 L0 540 Z" fill="url(#backFill)"/>
      <path d="M0 440 Q0 425 40 425 L973 425 L973 540 L0 540 Z" fill="url(#bandFill)"/>
      <path d="M0 590 L860 590 Q930 590 973 555 L973 1200 L0 1200 Z" fill="url(#frontFill)"/>
      <rect x="0" y="1030" width="973" height="170" fill="url(#footFill)"/>
    </svg>
    <div class="logo-name"><span class="logo-mark"></span>TROVALINE</div>
    <p class="back-website">www.TrovaLine.com</p>
  </section>

  <section class="card-front" aria-label="Card front">
    <div class="front-watermark">TROVALINE</div>
    <div class="logo-name"><span class="logo-mark"></span>TROVALINE</div>
    <h1 class="holder-name">MS. MARA ELLISON</h1>
    <p class="holder-title">CHIEF ADVISORY</p>
    <dl class="contact-list">
      <div class="contact-row"><dt>Phone</dt><span class="colon">:</span><dd>+1-877-555-0142</dd></div>
      <div class="contact-row"><dt>Email</dt><span class="colon">:</span><dd>mara@TrovaLine.com</dd></div>
      <div class="contact-row"><dt>Address</dt><span class="colon">:</span><dd class="address">TrovaLine.com<br>48 Harbor Lane, Suite 12<br>Portland, OR 97201</dd></div>
      <div class="contact-row"><dt>Website</dt><span class="colon">:</span><dd>www.TrovaLine.com</dd></div>
    </dl>
  </section>

</main>
</body>
</html>
```